Business Card Design

We need a design that will also transfer to car decals
We need a design that will speak to the average person needing home and office remodeling
The design should be fresh, exciting, easy to read in a glance and unique
We would like a die-cut tool belt
Bright colors and evenly spaced information

Target Market(s)

Home and business owners
Middle and Upper Income property owners
Families and people with fixer upper homes

Industry/Entity Type

Business

Contact Information for Business Card

Looking for the best Bay Area Handyman? Here I am!
RKW Handyman Services does it all at prices regular people can afford.
Electrical, Plumbing, Carpentry, Remodeling, Fencing, Picture and window placement, Hauling ... and anything else you can imagine!
510-374-2196
Serving the Entire Bay Area
Free Estimates! Call us Today to turn your dreams into reality!

Font styles to use
Serif

Requirements
Must have
• Speaks to the average person
stands out among similar industry cards
Nice to have
• fun, comical, you want to hold on to this card
Should not have
• bland colors
look too crowded

```html
<!DOCTYPE html>
<html lang="en">
<head>
<meta charset="utf-8">
<title>RKW Handyman Services – Business Card</title>
<link href="https://fonts.googleapis.com/css2?family=Orbitron:wght@700&family=Ubuntu+Condensed&family=Open+Sans:wght@500&display=swap" rel="stylesheet">
<style>
  :root {
    --stage: #d9d9d9;
    --ink: #111111;
    --yellow: #f5ea17;
    --pink: #e8186e;
    --band: #000000;
    --white: #ffffff;
    --badge-red: #d9232d;
    --belt-brown: #6b3f25;
    --belt-tan: #b09263;
    --pocket-orange: #e8802c;
  }
  html, body {
    margin: 0;
    width: 1200px;
    height: 1087px;
    overflow: hidden;
    background: var(--stage);
  }
  .card {
    position: absolute;
    left: 190px;
    width: 810px;
    height: 490px;
    box-sizing: border-box;
    border: 1px solid #8a8a8a;
    overflow: hidden;
  }
  .card--front {
    top: 47px;
    background: linear-gradient(to bottom, #ffffff 0%, #ffffff 50%, #bdbdbd 88%, #a9a9a9 100%);
  }
  .card--back {
    top: 552px;
    background: var(--yellow);
  }
  .title {
    position: absolute;
    left: 0;
    width: 100%;
    margin: 0;
    text-align: center;
    font-family: "Orbitron", sans-serif;
    font-weight: 700;
    font-size: 36px;
    letter-spacing: 2px;
    word-spacing: 10px;
    color: var(--ink);
  }
  .card--front .title { top: 190px; }
  .card--back .title { top: 46px; }
  .brand-mark {
    position: absolute;
    top: 82px;
    left: 0;
    width: 100%;
    display: flex;
    justify-content: center;
    align-items: center;
    gap: 10px;
    font-family: "Ubuntu Condensed", sans-serif;
    font-size: 26px;
    color: var(--badge-red);
  }
  .brand-mark .dot {
    width: 22px;
    height: 22px;
    border-radius: 50%;
    background: var(--badge-red);
  }
  .toolbelt-art {
    position: absolute;
    left: 155px;
    top: 258px;
    width: 475px;
    height: 150px;
    border-radius: 40px;
    background: linear-gradient(to bottom, var(--belt-tan) 0%, var(--belt-brown) 55%, var(--pocket-orange) 100%);
  }
  .footer {
    position: absolute;
    left: 0;
    bottom: 0;
    width: 100%;
    height: 52px;
    background: var(--band);
    border-top: 7px solid var(--pink);
    display: flex;
    justify-content: space-between;
    align-items: center;
    padding: 0 14px;
    box-sizing: content-box;
    font-family: "Open Sans", sans-serif;
    font-weight: 500;
    font-size: 20px;
    color: var(--white);
  }
  .footer { width: calc(100% - 28px); }
  .wrench {
    position: absolute;
    left: 298px;
    top: 106px;
  }
  .services, .tagline {
    position: absolute;
    left: 0;
    width: 100%;
    margin: 0;
    text-align: center;
    font-family: "Ubuntu Condensed", sans-serif;
    color: var(--ink);
  }
  .services { top: 164px; font-size: 27px; line-height: 32px; }
  .phone-big {
    position: absolute;
    top: 222px;
    left: 0;
    width: 100%;
    margin: 0;
    text-align: center;
    font-family: "Ubuntu Condensed", sans-serif;
    font-size: 104px;
    line-height: 110px;
    color: var(--ink);
  }
  .tagline { top: 330px; font-size: 25px; line-height: 32px; }
</style>
</head>
<body>

<section class="card card--front">
  <div class="brand-mark"><span class="dot"></span>RKW Handyman</div>
  <h1 class="title">RKW HANDYMAN SERVICES</h1>
  <div class="toolbelt-art" role="img" aria-label="Illustration of a brown leather tool belt with orange pockets holding a putty knife, hammer, wrench and paint roller"></div>
  <div class="footer">
    <span class="email">rkwhandyman@mailbox.com</span>
    <span class="contact">Contact: 510-374-2196</span>
  </div>
</section>

<section class="card card--back">
  <h2 class="title">RKW HANDYMAN SERVICES</h2>
  <svg class="wrench" width="214" height="42" viewBox="0 0 214 42" aria-hidden="true">
    <path d="M2 8 A20 20 0 1 0 30 30 L40 26 L40 16 L30 12 A20 20 0 0 0 2 8 Z M10 14 L22 14 L22 28 L10 28 Z" fill="var(--ink)" fill-rule="evenodd"/>
    <rect x="36" y="15" width="160" height="12" fill="var(--ink)"/>
    <circle cx="198" cy="21" r="12" fill="none" stroke="var(--ink)" stroke-width="6"/>
  </svg>
  <p class="services">Electrical, Plumbing, Carpentry, Remodeling, Fencing, Picture and<br>window placement, Hauling ... and anything else you can imagine!</p>
  <p class="phone-big">510-374-2196</p>
  <p class="tagline">Serving the Entire Bay Area. Get Free Estimates.<br>Call us Today to turn your Dreams into Reality...!</p>
  <div class="footer">
    <span class="email">rkwhandyman@mailbox.com</span>
    <span class="contact">Contact: 510-374-2196</span>
  </div>
</section>

</body>
</html>
```